Business Consultancy Business Card Design

Business Card design required for Business Analysis and Project Consultancy business based in Scotland.

Company Name - Brevick Advisory

Back - Company Logo

Front Details

Owen Brevick
07642 918 305
owen.brevick@brevickadvisory.com
http://www.brevickadvisory.com

Colours should match the logo colours but I am open to design ideas.

```html
<!DOCTYPE html>
<html lang="en">
<head>
<meta charset="utf-8">
<title>Brevick Advisory – Business Card</title>
<link href="https://fonts.googleapis.com/css2?family=Fira+Sans+Condensed:wght@400&family=Fira+Sans:wght@400&display=swap" rel="stylesheet">
<style>
  :root{
    --canvas:#ffffff;
    --plum-deep:#1c0f14;
    --plum:#3a1a24;
    --plum-warm:#5a2630;
    --rose-brown:#6e3034;
    --logo-grey:#7d7b7c;
    --mark-blue:#0a93d6;
    --ink-light:#ffffff;
  }
  *{margin:0;padding:0;box-sizing:border-box}
  html,body{width:1200px;height:1000px;overflow:hidden;background:var(--canvas)}
  .canvas{position:relative;width:1200px;height:1000px;background:var(--canvas)}

  .card{position:absolute;width:622px;height:367px;overflow:hidden;background:var(--plum-deep)}
  .card--back{left:301px;top:44px}
  .card--front{left:302px;top:441px}

  .card__backdrop{position:absolute;inset:0;
    background:linear-gradient(170deg,var(--plum-deep) 0%,var(--plum) 45%,var(--plum-warm) 75%,var(--rose-brown) 100%)}

  .brand{position:absolute;left:27px;top:64px;display:flex;align-items:center;gap:30px}
  .brand__dot{width:68px;height:68px;border-radius:50%;background:var(--mark-blue)}
  .brand__name{font-family:"Fira Sans",sans-serif;font-weight:400;font-size:42px;
    letter-spacing:1.5px;color:var(--logo-grey);text-transform:uppercase;white-space:nowrap}

  .name-band{position:absolute;left:0;right:0;top:106px;height:73px;
    background:linear-gradient(90deg,rgba(60,55,56,.85) 0%,rgba(100,95,96,.8) 55%,rgba(150,130,132,.85) 100%)}
  .holder{position:absolute;left:45px;top:119px;font-family:"Fira Sans Condensed",sans-serif;
    font-weight:400;font-size:38px;letter-spacing:3px;color:var(--ink-light);text-transform:uppercase;white-space:nowrap}
  .contact{position:absolute;left:45px;top:198px;list-style:none;
    font-family:"Fira Sans Condensed",sans-serif;font-weight:400;color:var(--ink-light);font-size:27px;line-height:37px;white-space:nowrap}
  .contact__phone{font-size:29px}
</style>
</head>
<body>
<div class="canvas">
  <section class="card card--back" aria-label="Card back">
    <div class="card__backdrop" role="img" aria-label="Abstract blurred light background in plum and warm red tones"></div>
    <div class="brand">
      <span class="brand__dot"></span>
      <span class="brand__name">Brevick Advisory</span>
    </div>
  </section>

  <section class="card card--front" aria-label="Card front">
    <div class="card__backdrop" role="img" aria-label="Abstract blurred light background in plum and warm red tones"></div>
    <div class="name-band"></div>
    <h1 class="holder">Owen Brevick</h1>
    <ul class="contact">
      <li class="contact__phone">07642 918 305</li>
      <li class="contact__email">owen.brevick@brevickadvisory.com</li>
      <li class="contact__web">http://www.brevickadvisory.com</li>
    </ul>
  </section>
</div>
</body>
</html>
```